Biotech company needs graphics to describe company culture

We would like to have help in describing our company culture in a graphic way.Our "local culture" focus areas (Proud & Accountable, Challenge & Collaborate) builds on the Corvane Halbrook corporate values which is Integrity, Intensity, Innovation and Involvement. Our "local norms" is describing behaviours which we want to see more of, and that will ensure that we get better at our culture focus. We would like this to be expressed in a graphic way, getting an image we can use for multiple purposes in a format that fits into PowerPoint slides, can be printed on mousepads etc. We want one Norwegian and one English version. Attached is an example of the desired content in both languages.

Target Market(s)

Employees

Industry/Entity Type

Biotechnology

Font styles to use
Serif

Colors

Designer to choose colors to be used in the design.

Requirements
Nice to have
• Want the employees to intuitive understand the connection from values to cultural focus to norms. The norms are the most important to highlight to our employees. They should understand that if they do more of the desired behaviours (norms), then they will have act according to our culture focus and our values.

```html
<!DOCTYPE html>
<html lang="en">
<head>
<meta charset="utf-8">
<title>Our Culture – Vår Kultur</title>
<link rel="stylesheet" href="https://fonts.googleapis.com/css2?family=Bebas+Neue&family=Poppins:wght@600;700&display=swap">
<style>
  :root {
    --stage: #6d6e70;
    --paper: #ffffff;
    --red: #ea3d33;
    --navy: #2e3583;
    --blue: #1c75bb;
    --ink: #1f1f22;
    --rail: #e3e4e5;
    --box: #e6e7e8;
  }
  html, body { margin: 0; padding: 0; overflow: hidden; }
  body {
    width: 839px; height: 1200px;
    background: var(--stage);
    position: relative;
  }
  .card { position: absolute; left: 87px; width: 665px; height: 470px; display: block; }
  .card--en { top: 112px; }
  .card--no { top: 617px; }
  .title { font-family: "Bebas Neue", sans-serif; font-size: 80px; fill: #000; text-anchor: middle; }
  .band-label { font-family: "Bebas Neue", sans-serif; font-size: 36px; fill: #fff; text-anchor: middle; }
  .pill-label { font-family: "Poppins", sans-serif; font-weight: 700; font-size: 19px; fill: #fff; text-anchor: middle; }
  .focus-label { font-family: "Poppins", sans-serif; font-weight: 700; font-size: 16px; fill: #fff; text-anchor: middle; }
  .card--no .focus-label { font-size: 19px; }
  .norm-text { font-family: "Poppins", sans-serif; font-weight: 700; font-size: 15px; fill: var(--ink); }
  .card--no .norm-text { font-size: 13px; }
  .hl-blue { fill: var(--blue); }
  .hl-red { fill: var(--red); }
  .hl-navy { fill: var(--navy); }
  .norm-num { font-family: "Bebas Neue", sans-serif; font-size: 50px; fill: #fff; text-anchor: middle; }
  .brand { font-family: "Poppins", sans-serif; font-weight: 700; font-size: 28px; fill: var(--red); text-anchor: middle; }
  .rail { stroke: var(--rail); stroke-width: 5; fill: none; }
</style>
</head>
<body>

<!-- English version -->
<svg class="card card--en" viewBox="0 0 1000 707" aria-labelledby="en-title">
  <rect width="1000" height="707" fill="var(--paper)"/>
  <path d="M362 0H639V12Q639 27 624 27H377Q362 27 362 12Z" fill="var(--red)"/>
  <text id="en-title" class="title" x="501" y="106">OUR CULTURE</text>

  <polygon points="0,122 322,122 332,151.5 322,181 0,181" fill="var(--red)"/>
  <polygon points="327,122 670,122 680,151.5 670,181 327,181 337,151.5" fill="var(--navy)"/>
  <polygon points="675,122 1000,122 1000,181 675,181 685,151.5" fill="var(--blue)"/>
  <text class="band-label" x="184" y="164">OUR VALUES</text>
  <text class="band-label" x="502" y="164">OUR CULTURE FOCUS</text>
  <text class="band-label" x="826" y="164">OUR NORMS</text>

  <path class="rail" d="M270 318H305V531H270M305 432H365M365 318V531M570 318H602V531H570M602 432H641M697 270H641V590H697"/>
  <path class="rail" d="M365 318H389M365 531H389"/>
  <circle cx="337" cy="432" r="9" fill="var(--red)"/>
  <circle cx="641" cy="432" r="9" fill="var(--red)"/>

  <g class="values">
    <path d="M113 294H270V342H113A24 24 0 0 1 113 294Z" fill="var(--red)"/><text class="pill-label" x="180" y="325">INTEGRITY</text>
    <path d="M113 366H270V414H113A24 24 0 0 1 113 366Z" fill="var(--red)"/><text class="pill-label" x="186" y="397">INTENSITY</text>
    <path d="M113 438H270V486H113A24 24 0 0 1 113 438Z" fill="var(--red)"/><text class="pill-label" x="181" y="469">INNOVATION</text>
    <path d="M113 505H270V553H113A24 24 0 0 1 113 505Z" fill="var(--red)"/><text class="pill-label" x="183" y="536">INVOLVEMENT</text>
  </g>

  <g class="focus">
    <path d="M409 294H550Q570 294 570 314V342H389V314Q389 294 409 294Z" fill="var(--navy)"/><text class="focus-label" x="478" y="325">PROUD</text>
    <path d="M409 364H550Q570 364 570 384V412H389V384Q389 364 409 364Z" fill="var(--navy)"/><text class="focus-label" x="484" y="393">ACCOUNTABLE</text>
    <path d="M409 433H550Q570 433 570 453V481H389V453Q389 433 409 433Z" fill="var(--navy)"/><text class="focus-label" x="481" y="462">CHALLENGE</text>
    <path d="M409 506H550Q570 506 570 526V554H389V526Q389 506 409 506Z" fill="var(--navy)"/><text class="focus-label" x="479" y="535">COLLABORATE</text>
  </g>

  <g class="norms">
    <rect x="697" y="213" width="200" height="116" rx="12" fill="var(--box)"/>
    <rect x="864" y="211" width="52" height="120" rx="24" fill="var(--blue)"/>
    <text class="norm-num" x="891" y="290">01</text>
    <text class="norm-text" x="712" y="242">
      <tspan x="712">I TAKE OWNERSHIP,</tspan>
      <tspan x="712" dy="17">AM <tspan class="hl-blue">SOLUTION</tspan></tspan>
      <tspan x="712" dy="17"><tspan class="hl-blue">ORIENTED</tspan> AND</tspan>
      <tspan x="712" dy="17">ENSURE</tspan>
      <tspan x="712" dy="17">IMPLEMENTATION</tspan>
    </text>

    <rect x="693" y="375" width="204" height="113" rx="12" fill="var(--box)"/>
    <rect x="864" y="373" width="52" height="120" rx="24" fill="var(--red)"/>
    <text class="norm-num" x="890" y="450">02</text>
    <text class="norm-text" x="712" y="421">
      <tspan x="712">I GIVE AND SEEK</tspan>
      <tspan x="712" dy="17" class="hl-red">CONSTRUCTIVE</tspan>
      <tspan x="712" dy="17" class="hl-red">FEEDBACK</tspan>
    </text>

    <rect x="697" y="534" width="200" height="116" rx="12" fill="var(--box)"/>
    <rect x="864" y="531" width="52" height="120" rx="24" fill="var(--navy)"/>
    <text class="norm-num" x="891" y="610">03</text>
    <text class="norm-text" x="712" y="566">
      <tspan x="712">I AM <tspan class="hl-navy">CURIOUS</tspan></tspan>
      <tspan x="712" dy="17">ABOUT OTHERS</tspan>
      <tspan x="712" dy="17">PERSPECTIVES</tspan>
      <tspan x="712" dy="17">AND NEW WAYS</tspan>
      <tspan x="712" dy="17">OF DOING THINGS</tspan>
    </text>
  </g>

  <path d="M0 666H40Q40 690 64 690H290V707H0Z" fill="var(--rail)"/>
  <rect x="290" y="666" width="710" height="41" fill="var(--rail)"/>
  <text class="brand" x="164" y="654">Corvane Halbrook</text>
</svg>

<!-- Norwegian version -->
<svg class="card card--no" viewBox="0 0 1000 707" aria-labelledby="no-title">
  <rect width="1000" height="707" fill="var(--paper)"/>
  <path d="M362 0H639V12Q639 27 624 27H377Q362 27 362 12Z" fill="var(--red)"/>
  <text id="no-title" class="title" x="501" y="106">VÅR KULTUR</text>

  <polygon points="0,122 322,122 332,151.5 322,181 0,181" fill="var(--red)"/>
  <polygon points="327,122 670,122 680,151.5 670,181 327,181 337,151.5" fill="var(--navy)"/>
  <polygon points="675,122 1000,122 1000,181 675,181 685,151.5" fill="var(--blue)"/>
  <text class="band-label" x="158" y="164">VÅRE VERDIER</text>
  <text class="band-label" x="507" y="164">VÅRT KULTURFOKUS</text>
  <text class="band-label" x="826" y="164">VÅRE NORMER</text>

  <path class="rail" d="M270 318H305V531H270M305 432H365M365 318V531M570 318H602V531H570M602 432H641M697 270H641V590H697"/>
  <path class="rail" d="M365 318H389M365 531H389"/>
  <circle cx="337" cy="432" r="9" fill="var(--red)"/>
  <circle cx="641" cy="432" r="9" fill="var(--red)"/>

  <g class="values">
    <path d="M113 294H270V342H113A24 24 0 0 1 113 294Z" fill="var(--red)"/><text class="pill-label" x="180" y="325">INTEGRITY</text>
    <path d="M113 366H270V414H113A24 24 0 0 1 113 366Z" fill="var(--red)"/><text class="pill-label" x="186" y="397">INTENSITY</text>
    <path d="M113 438H270V486H113A24 24 0 0 1 113 438Z" fill="var(--red)"/><text class="pill-label" x="181" y="469">INNOVATION</text>
    <path d="M113 505H270V553H113A24 24 0 0 1 113 505Z" fill="var(--red)"/><text class="pill-label" x="183" y="536">INVOLVEMENT</text>
  </g>

  <g class="focus">
    <path d="M409 294H550Q570 294 570 314V342H389V314Q389 294 409 294Z" fill="var(--navy)"/><text class="focus-label" x="477" y="325">STOLT</text>
    <path d="M409 364H550Q570 364 570 384V412H389V384Q389 364 409 364Z" fill="var(--navy)"/><text class="focus-label" x="477" y="394">ANSVARLIG</text>
    <path d="M409 433H550Q570 433 570 453V481H389V453Q389 433 409 433Z" fill="var(--navy)"/><text class="focus-label" x="478" y="464">UTFORDRER</text>
    <path d="M409 506H550Q570 506 570 526V554H389V526Q389 506 409 506Z" fill="var(--navy)"/><text class="focus-label" x="480" y="536">SAMHANDLER</text>
  </g>

  <g class="norms">
    <rect x="697" y="213" width="200" height="116" rx="12" fill="var(--box)"/>
    <rect x="864" y="211" width="52" height="120" rx="24" fill="var(--blue)"/>
    <text class="norm-num" x="891" y="290">01</text>
    <text class="norm-text" x="712" y="254">
      <tspan x="712">JEG TAR EIERSKAP, ER</tspan>
      <tspan x="712" dy="17" class="hl-blue">LØSNINGSORIENTERT</tspan>
      <tspan x="712" dy="17">OG SIKRER</tspan>
      <tspan x="712" dy="17">GJENNOMFØRING</tspan>
    </text>

    <rect x="693" y="375" width="204" height="113" rx="12" fill="var(--box)"/>
    <rect x="864" y="373" width="52" height="120" rx="24" fill="var(--red)"/>
    <text class="norm-num" x="890" y="450">02</text>
    <text class="norm-text" x="712" y="420">
      <tspan x="712">JEG GIR OG SØKER</tspan>
      <tspan x="712" dy="17">KONSTRUKTIVE</tspan>
      <tspan x="712" dy="17" class="hl-red">TILBAKEMELDINGER</tspan>
    </text>

    <rect x="697" y="534" width="200" height="116" rx="12" fill="var(--box)"/>
    <rect x="864" y="531" width="52" height="120" rx="24" fill="var(--navy)"/>
    <text class="norm-num" x="891" y="610">03</text>
    <text class="norm-text" x="712" y="563">
      <tspan x="712">JEG ER <tspan class="hl-navy">NYSGJERRIG</tspan></tspan>
      <tspan x="712" dy="17">PÅ ANDRES</tspan>
      <tspan x="712" dy="17">PERSPEKTIVER OG</tspan>
      <tspan x="712" dy="17">NYE MÅTER Å GJØRE</tspan>
      <tspan x="712" dy="17">TING PÅ</tspan>
    </text>
  </g>

  <path d="M0 666H40Q40 690 64 690H290V707H0Z" fill="var(--rail)"/>
  <rect x="290" y="666" width="710" height="41" fill="var(--rail)"/>
  <text class="brand" x="164" y="654">Corvane Halbrook</text>
</svg>

</body>
</html>
```